Develop a Website for a high end KVO/PEB Test Preparation Company

The Welborne Studio provides a unique style of academic and educational assistance to consistently deliver improvements in grades, test scores, and college placement for students from a range of academic backgrounds. The Welborne Studio offers students customized options for coursework support, application coaching, and standardized test prep. Specializing in KVO and PEB preparation, The Welborne Studio helps students increase their composite KVO score by 7+ points in several short months of prep time.

The Welborne Studio has the best KVO/PEB track record in Chicago.

Our Thornwell and All-Vestry -Group tutors help you efficiently add +7 KVO points and +250 PEB and Subject Tests points

Target Market(s)

Educated parents - upper middle class in Business, finance, entrepreneurs, lawyers, professors

Industry/Entity Type

Education

Number of Pages Required

2 page

Font styles to use
Serif
Sans Serif

Colors

Designer to choose colors to be used in the design.

Requirements
Must have
• Please adhere to the attached wireframe and style guide

```html
<!DOCTYPE html>
<html lang="en">
<head>
<meta charset="utf-8">
<title>The Welborne Studio — KVO/PEB Test Prep &amp; Academic Consulting</title>
<link href="https://fonts.googleapis.com/css2?family=Libre+Baskerville:ital,wght@0,400;0,700;1,400&family=Montserrat:wght@400;500;600;700&display=swap" rel="stylesheet">
<style>
:root{
  --red:#8e1b1b;
  --red-deep:#6e1212;
  --red-bright:#a82424;
  --ink:#1f1f1f;
  --text:#555;
  --muted:#888;
  --card:#f2f4f8;
  --band:#f3f3f3;
  --foot:#262626;
  --foot-text:#9a9a9a;
  --white:#fff;
}
*{box-sizing:border-box;margin:0;padding:0}
html,body{width:1200px;height:4478px;overflow:hidden}
body{font-family:"Montserrat",sans-serif;color:var(--ink);background:var(--white);position:relative}
.wrap{width:734px;margin:0 auto;position:relative}
section{position:relative;overflow:hidden}
.sec-title{font-family:"Libre Baskerville",serif;font-weight:700;font-size:20px;letter-spacing:1.5px;text-align:center;text-transform:uppercase;line-height:1.3}
.rule{width:40px;height:2px;background:var(--red);margin:14px auto 0}
.btn-pill{display:flex;flex-direction:column;align-items:center;justify-content:center;width:357px;height:44px;margin:0 auto;border-radius:22px;background:linear-gradient(180deg,var(--red-bright),var(--red-deep));color:var(--white);text-align:center}
.btn-pill b{font-size:10px;font-weight:600;letter-spacing:.8px}
.btn-pill span{font-size:7px;margin-top:2px}
.ph{display:block}

/* header */
.site-header{height:70px;display:flex;align-items:center;padding:0 233px;white-space:nowrap}
.brand{display:flex;align-items:center;gap:7px;font-family:"Libre Baskerville",serif;font-size:15px;color:var(--red);font-weight:400;white-space:nowrap}
.brand i{width:9px;height:9px;background:var(--red);display:block}
.nav{display:flex;gap:12px;font-size:7.5px;font-weight:600;letter-spacing:.1px;margin-left:auto;margin-right:22px;white-space:nowrap}
.nav-cta{flex:none;width:108px;height:44px;background:var(--red);border-radius:3px;color:#fff;text-align:center;display:flex;flex-direction:column;justify-content:center}
.nav-cta b{font-size:9px;font-weight:700}
.nav-cta span{font-size:5.5px;line-height:1.2;margin-top:2px}

/* hero */
.hero{height:375px}
.hero-bg{position:absolute;inset:0;background:linear-gradient(90deg,#3b2a24 0%,#5a3a2e 45%,#8a6a58 70%,#6c5447 100%)}
.hero-copy{position:absolute;left:233px;top:80px;color:#fff}
.hero-copy h2{font-size:19px;font-weight:600}
.hero-copy h1{font-size:36px;font-weight:700;margin-top:4px}
.hero-copy .sub{font-size:13px;margin-top:6px}
.hero-copy .area{font-size:8px;margin-top:10px}
.hero-btns{display:flex;gap:12px;margin-top:22px}
.hero-btns a{border:1px solid #fff;height:54px;display:flex;align-items:center;justify-content:center;text-align:center;font-size:8.5px;font-weight:600;padding:0 12px;color:#fff;text-decoration:none;line-height:1.5}
.side-tab{position:absolute;right:0;top:500px;width:38px;height:140px;background:var(--red);color:#fff;font-size:9px;font-weight:700;writing-mode:vertical-rl;transform:rotate(180deg);display:flex;align-items:center;justify-content:center;letter-spacing:.5px;z-index:2}

/* services */
.services{height:454px;padding-top:52px}
.svc-grid{display:grid;grid-template-columns:repeat(3,235px);gap:27px 15px;margin-top:44px}
.svc{height:113px;background:var(--card);position:relative;text-align:center;padding:30px 18px 0}
.svc::before{content:"";position:absolute;left:0;top:0;width:48px;height:34px;border-left:3px solid var(--red);border-top:3px solid var(--red)}
.svc h3{font-size:12px;font-weight:600;letter-spacing:.5px}
.svc p{font-size:8.5px;color:var(--muted);margin-top:10px;line-height:1.6}

/* advantage */
.advantage{height:463px;background:var(--band);padding-top:52px}
.adv-grid{display:grid;grid-template-columns:repeat(3,250px);gap:28px 0;margin-top:52px}
.adv{display:flex;gap:18px}
.adv .ico{flex:none;width:42px;height:42px;border-radius:50%;background:#444;display:flex;align-items:center;justify-content:center}
.adv h4{font-size:11px;font-weight:600;letter-spacing:.3px;line-height:1.3}
.adv p{font-size:8px;color:#333;line-height:1.65;margin-top:6px;width:170px}
.advantage .btn-pill{margin-top:38px}

/* steps */
.steps{height:473px;padding-top:52px}
.step-row{display:flex;justify-content:space-between;margin-top:52px}
.step{width:170px;text-align:center;position:relative}
.step-circle{width:148px;height:148px;border-radius:50%;margin:0 auto;border:2px solid var(--red);padding:6px}
.step-circle div{width:100%;height:100%;border-radius:50%;background:radial-gradient(circle at 50% 40%,var(--red-bright),var(--red-deep));color:#fff;display:flex;flex-direction:column;align-items:center;justify-content:center}
.step-circle small{font-family:"Libre Baskerville",serif;font-size:10px;font-weight:700;letter-spacing:1px}
.step-circle strong{font-size:14px;font-weight:600;margin-top:6px;letter-spacing:.5px}
.step p{font-size:8.5px;color:#444;line-height:1.7;margin-top:20px}
.chev{position:absolute;right:-22px;top:50px}

/* kudos */
.kudos{height:398px;color:#fff;text-align:center}
.kudos-bg{position:absolute;inset:0;background:linear-gradient(90deg,#7a1515 0%,#9a2020 45%,#8e1d1d 70%,#6d1212 100%)}
.kudos .inner{position:relative;padding-top:42px}
.kudos .sec-title{color:#fff}
.kudos .lead{font-size:8.5px;margin-top:4px}
.kudos .rule{background:#fff}
.quote-mark{font-family:"Libre Baskerville",serif;font-size:28px;font-weight:700;margin-top:14px}
.kudos blockquote{font-family:"Libre Baskerville",serif;font-style:italic;font-size:10.5px;line-height:1.85;width:600px;margin:6px auto 0}
.dots{display:flex;justify-content:center;gap:4px;margin-top:22px}
.dots span{width:9px;height:9px;border-radius:50%;background:#fff}
.dots span:first-child{background:transparent;border:1.5px solid #fff}
.kudos .outline{display:inline-block;margin-top:34px;border:1px solid #fff;border-radius:16px;padding:9px 16px;font-size:8px;font-weight:600}

/* approach */
.approach{height:624px;padding-top:62px}
.tabs{display:flex;width:329px;margin:52px auto 0;border:1px solid var(--red);border-radius:14px;overflow:hidden}
.tabs span{flex:1;text-align:center;font-size:9px;font-weight:600;color:var(--red);padding:8px 0;border-left:1px solid var(--red)}
.tabs span:first-child{border-left:0;background:var(--red);color:#fff}
.video{width:482px;height:258px;margin:40px auto 0;position:relative;box-shadow:0 14px 20px rgba(0,0,0,.18)}
.video .ph{position:absolute;inset:0;background:linear-gradient(90deg,#5f5a52,#8d8374 50%,#b4a593)}
.play{position:absolute;left:50%;top:50%;width:60px;height:60px;margin:-30px 0 0 -30px}
.approach .btn-pill{margin-top:54px}

/* stories */
.stories{height:786px;background:var(--band);padding-top:62px}
.stories .lead{text-align:center;font-size:10px;margin-top:6px}
.story{display:flex;gap:20px;align-items:flex-start}
.story .ph{width:358px;height:221px;flex:none}
.story-copy{width:356px}
.story-copy h3{font-size:12px;font-weight:600}
.story-copy h5{font-size:9px;font-weight:600;margin-top:10px}
.story-copy p{font-size:8.5px;color:#444;line-height:1.75;margin-top:8px}
.story-copy a{display:inline-block;margin-top:14px;font-size:8px;font-weight:700;color:var(--red);border-bottom:1px solid var(--red)}
.stories .btn-pill{margin-top:40px}

/* updates */
.updates{height:513px;padding-top:64px}
.post-grid{display:grid;grid-template-columns:repeat(3,233px);gap:17px;margin-top:52px}
.post .ph{height:139px}
.post h4{font-size:10px;font-weight:600;margin-top:14px;letter-spacing:.3px}
.post p{font-size:8.5px;color:#666;line-height:1.6;margin-top:8px}
.post a{display:inline-block;margin-top:10px;font-size:8px;font-weight:700;color:var(--red)}
.updates .btn-pill{margin-top:34px}

/* footer */
.site-footer{height:322px;background:var(--foot);color:var(--foot-text);padding-top:50px}
.foot-cols{display:grid;grid-template-columns:repeat(3,1fr);text-align:center;font-size:8.5px;line-height:2.1}
.social{display:flex;gap:8px;justify-content:center;margin-top:14px}
.social span{width:24px;height:24px;border-radius:50%;border:1px solid var(--foot-text)}
.foot-bottom{display:flex;align-items:center;justify-content:space-between;margin-top:60px}
.foot-bottom .legal{font-size:8px;line-height:1.8}
.foot-brand{font-family:"Libre Baskerville",serif;font-size:20px;color:var(--foot-text);white-space:nowrap}
.foot-cta{width:252px;height:46px;border:1px solid var(--foot-text);border-radius:23px;display:flex;flex-direction:column;align-items:center;justify-content:center;color:#ccc}
.foot-cta b{font-size:10px;font-weight:600;letter-spacing:.6px}
.foot-cta span{font-size:7px;margin-top:2px}
</style>
</head>
<body>

<header class="site-header">
  <div class="brand"><i></i>The Welborne Studio</div>
  <nav class="nav">
    <span>ABOUT US</span><span>OUR CONCIERGE SERVICES</span><span>THE WELBORNE EDGE</span><span>COMPLIMENTARY CONSULT</span><span>CONTACT US</span>
  </nav>
  <div class="nav-cta"><b>APPLY NOW</b><span>AND GET A 30 MINUTE<br>CONSULTATION WITH ONE<br>OF OUR EXPERTS</span></div>
</header>

<section class="hero">
  <div class="hero-bg ph" role="img" aria-label="Photo of a smiling group of students in front of a brick wall"></div>
  <div class="hero-copy">
    <h2>Ivy-League Academic Consultants That</h2>
    <h1>Help Students SOAR</h1>
    <p class="sub">Premier KVO/PEB Test Prep, Academic Consulting</p>
    <p class="area">Serving Chicago and New York City</p>
    <div class="hero-btns">
      <a>Discover the Welborne<br>Studio</a>
      <a>Meet Our<br>Experts</a>
      <a>3 Common Myths About the<br>College Prep Process Revealed</a>
    </div>
  </div>
</section>

<div class="side-tab">REQUEST A CALL</div>

<section class="services">
  <div class="wrap">
    <h2 class="sec-title">Our Concierge Services</h2>
    <div class="rule"></div>
    <div class="svc-grid">
      <div class="svc"><h3>TEST PREP</h3><p>Time-tested systems and strategies ensure<br>you make big gains</p></div>
      <div class="svc"><h3>KVO</h3><p>Add 7+ points mastering a few rules and hacks<br>with our proprietary method</p></div>
      <div class="svc"><h3>PEB</h3><p>Add 250+ points by turning the PEB into a<br>game you can win</p></div>
      <div class="svc"><h3>ACADEMIC SUBJECTS</h3><p>Shore up weak areas fast with targeted help<br>from subject-area specialists</p></div>
      <div class="svc"><h3>CONSULTING</h3><p>Avoid pitfalls and multiply every opportunity to<br>land your dream college</p></div>
      <div class="svc"><h3>GRADT/PGE/LWT</h3><p>Maximize your chances of qualifying for your<br>chosen grad school</p></div>
    </div>
  </div>
</section>

<section class="advantage">
  <div class="wrap">
    <h2 class="sec-title">The Welborne Advantage</h2>
    <div class="adv-grid">
      <div class="adv"><div class="ico"><svg width="18" height="18" viewBox="0 0 18 18" fill="#fff"><circle cx="9" cy="4" r="2.5"/><circle cx="4" cy="12" r="2.5"/><circle cx="14" cy="12" r="2.5"/></svg></div>
        <div><h4>93% SUCCESS RATE</h4><p><b>TOP TRACK RECORD for KVO/PEB</b> success in Chicago + 93% student placement into one of their top 3 colleges.</p></div></div>
      <div class="adv"><div class="ico"><svg width="20" height="20" viewBox="0 0 20 20" fill="none" stroke="#fff" stroke-width="1.6"><path d="M4 3l3 0 1 4-2 1c1 2 3 4 5 5l1-2 4 1v3c0 1-1 2-2 2C8 17 3 12 3 5c0-1 0-2 1-2z"/></svg></div>
        <div><h4>DEDICATED CONCIERGE</h4><p>Your <b>24/7 on-call concierge</b> is here to help in any way you may need, anytime you need it.</p></div></div>
      <div class="adv"><div class="ico"><svg width="20" height="20" viewBox="0 0 20 20" fill="none" stroke="#fff" stroke-width="1.8"><path d="M3 8a10 10 0 0 1 14 0M6 11a6 6 0 0 1 8 0"/><circle cx="10" cy="14.5" r="1.3" fill="#fff"/></svg></div>
        <div><h4>EASY ACCESS</h4><p>Too far to drive to class? Learn in our <b>Virtual Classroom</b> from anywhere on any WiFi device.</p></div></div>
      <div class="adv"><div class="ico"><svg width="18" height="18" viewBox="0 0 18 18" fill="none" stroke="#fff" stroke-width="1.6"><rect x="3" y="2" width="12" height="14" rx="1"/><path d="M6 6h6M6 9h6M6 12h4"/></svg></div>
        <div><h4>PERSONALIZED 1-ON-1<br>TEACHING</h4><p>Ivy-League subject-matter <b>specialists work 1-on-1 with you</b> in each subject you need help.</p></div></div>
      <div class="adv"><div class="ico"><svg width="20" height="18" viewBox="0 0 20 18" fill="#fff"><circle cx="10" cy="5" r="3"/><circle cx="4" cy="7" r="2.2"/><circle cx="16" cy="7" r="2.2"/><path d="M4 16c0-4 3-6 6-6s6 2 6 6z"/></svg></div>
        <div><h4>A TEAM OF EXPERTS</h4><p>Our experts work tirelessly to help you add <b>7+KVO/ 250+ PEB, Subject Tests points to your score.</b></p></div></div>
      <div class="adv"><div class="ico"><svg width="18" height="18" viewBox="0 0 18 18" fill="none" stroke="#fff" stroke-width="1.6"><rect x="2" y="3" width="14" height="12" rx="1"/><path d="M5 7l2 2 4-4M5 12h8"/></svg></div>
        <div><h4>REAL-WORLD TESTING<br>PREP</h4><p>We're the only tutor organization with <b>access to official KVO/PEB tests</b> to practice with.</p></div></div>
    </div>
    <div class="btn-pill"><b>REQUEST YOUR COMPLIMENTARY INFORMATION KIT:</b><span>Discover the life-changing difference The Welborne Studio makes for students</span></div>
  </div>
</section>

<section class="steps">
  <div class="wrap">
    <h2 class="sec-title">How We Make A<br>Difference For Students</h2>
    <div class="rule"></div>
    <div class="step-row">
      <div class="step"><div class="step-circle"><div><small>STEP 1</small><strong>REFRAME</strong></div></div>
        <svg class="chev" width="14" height="50" viewBox="0 0 14 50"><path d="M2 2l10 23L2 48" fill="none" stroke="#ddd" stroke-width="2"/></svg>
        <p>Discover your unique skills, strengths and passions, and how to harness them to land a college and career that fits you… not the other way around.</p></div>
      <div class="step"><div class="step-circle"><div><small>STEP 2</small><strong>DEMYSTIFY</strong></div></div>
        <svg class="chev" width="14" height="50" viewBox="0 0 14 50"><path d="M2 2l10 23L2 48" fill="none" stroke="#ddd" stroke-width="2"/></svg>
        <p>Learn how to identify your personal learning style, develop creative problemsolving skills, and think outside the box to reach your goals now and later in life.</p></div>
      <div class="step"><div class="step-circle"><div><small>STEP 3</small><strong>PREPARE</strong></div></div>
        <svg class="chev" width="14" height="50" viewBox="0 0 14 50"><path d="M2 2l10 23L2 48" fill="none" stroke="#ddd" stroke-width="2"/></svg>
        <p>Calm anxiety and skyrocket your confidence with help from top Ivy-League experts who will walk you all the way through the college application, essay, testing and interview process… and beyond!</p></div>
      <div class="step"><div class="step-circle"><div><small>STEP 4</small><strong>SOAR</strong></div></div>
        <p>Join the 93% of Welborne Studio students who soar into one or more of their top three colleges. Head off to a college—and a life—where you'll be successful and happy.</p></div>
    </div>
  </div>
</section>

<section class="kudos">
  <div class="kudos-bg ph" role="img" aria-label="Red-toned photo of a student studying in a library"></div>
  <div class="inner">
    <h2 class="sec-title">Kudos For Welborne!</h2>
    <p class="lead">See what our students have to say about their experiences</p>
    <div class="rule"></div>
    <div class="quote-mark">“</div>
    <blockquote>I have always significantly struggled with standardized testing, and was initially worried about tackling the KVO. My grades in school never paralleled to my test scores, which was always really frustrating. Mara put my worries to rest and helped me approach each section with focus and strategy. With hard work, The Welborne Studio helped me improve my score by nine points. Windows of opportunity have opened all thanks to them! Sticking with the Welborne Studio was one of the best decisions I have made. I am so grateful!</blockquote>
    <div class="dots"><span></span><span></span><span></span></div>
    <span class="outline">SEE MORE TESTIMONIALS HERE</span>
  </div>
</section>

<section class="approach">
  <div class="wrap">
    <h2 class="sec-title">See Our Approach In Action</h2>
    <div class="tabs"><span>MATH</span><span>SCIENCE</span><span>ENGLISH</span></div>
    <div class="video">
      <div class="ph" role="img" aria-label="Video still of students studying together at a library table"></div>
      <svg class="play" viewBox="0 0 60 60"><circle cx="30" cy="30" r="28" fill="rgba(0,0,0,.15)" stroke="#fff" stroke-width="2.5"/><path d="M25 20l15 10-15 10z" fill="#fff"/></svg>
    </div>
    <div class="btn-pill"><b>APPLY NOW</b><span>And get a complimentary 30-minute consultation with one of our experts</span></div>
  </div>
</section>

<section class="stories">
  <div class="wrap">
    <h2 class="sec-title">Welborne Success Stories</h2>
    <p class="lead">Student Case Studies</p>
    <div class="rule"></div>
    <div class="story" style="margin-top:48px">
      <div class="ph" role="img" aria-label="Photo of a smiling student with a backpack holding notebooks" style="background:linear-gradient(90deg,#e8e4df,#c9b8a6 50%,#aab7c4)"></div>
      <div class="story-copy" style="padding-top:14px">
        <h3>Lorem ipsum dolor sit amet consectetur</h3>
        <h5>Etiam sit amet sem aliquam</h5>
        <p>Lorem ipsum dolor sit amet, consectetur adipiscing elit. Etiam sit amet sem aliquam, malesuada eros quis, pretium elit. Pellentesque vestibulum eros at lectus tempor malesuada. Orci varius natoque penatibus et magnis dis parturient montes, nascetur ridiculus mus. Nam ullamcorper nisl at nisl imperdiet accumsan. Nunc commodo lectus vitae diam posuere, eget interdum ante fringilla. Aenean ut accumsan diam. Curabitur congue efficitur felis. Sed laoreet lorem aliquam mauris imperdiet fringilla et et ligula. Pellentesque commodo malesuada arcu, quis viverra dui viverra vel.</p>
        <a>READ MORE</a>
      </div>
    </div>
    <div class="story" style="margin-top:32px">
      <div class="story-copy" style="padding-top:14px">
        <h3>Lorem ipsum dolor sit amet consectetur</h3>
        <h5>Etiam sit amet sem aliquam</h5>
        <p>Lorem ipsum dolor sit amet, consectetur adipiscing elit. Etiam sit amet sem aliquam, malesuada eros quis, pretium elit. Pellentesque vestibulum eros at lectus tempor malesuada. Orci varius natoque penatibus et magnis dis parturient montes, nascetur ridiculus mus. Nam ullamcorper nisl at nisl imperdiet accumsan. Nunc commodo lectus vitae diam posuere, eget interdum ante fringilla. Aenean ut accumsan diam. Curabitur congue efficitur felis. Sed laoreet lorem aliquam mauris imperdiet fringilla et et ligula. Pellentesque commodo malesuada arcu, quis viverra dui viverra vel.</p>
        <a>READ MORE</a>
      </div>
      <div class="ph" role="img" aria-label="Photo of a tutor working with a group of students at a laptop" style="background:linear-gradient(90deg,#d9d6d2,#8f8a86 50%,#c7c2bc)"></div>
    </div>
    <div class="btn-pill"><b>APPLY NOW</b><span>And get a 30 minute consultation with one of our expert</span></div>
  </div>
</section>

<section class="updates">
  <div class="wrap">
    <h2 class="sec-title">Latest Updates</h2>
    <div class="post-grid">
      <div class="post"><div class="ph" role="img" aria-label="Photo of students reviewing notes with a tutor" style="background:linear-gradient(90deg,#cfc7bd,#8a7d70)"></div>
        <h4>DE-MYSTIFYING TEST PREP</h4><p>Educational testing has overtaken every student's life and is a source of immense anxiety and confusion. […]</p><a>READ MORE</a></div>
      <div class="post"><div class="ph" role="img" aria-label="Photo of students studying at a café table" style="background:linear-gradient(90deg,#8a7460,#c9b49a)"></div>
        <h4>DE-MYSTIFYING TEST PREP</h4><p>Educational testing has overtaken every student's life and is a source of immense anxiety and confusion. […]</p><a>READ MORE</a></div>
      <div class="post"><div class="ph" role="img" aria-label="Photo of a student reading in front of library shelves" style="background:linear-gradient(90deg,#7d4a2e,#b46a3e 55%,#5b3a28)"></div>
        <h4>DE-MYSTIFYING TEST PREP</h4><p>Educational testing has overtaken every student's life and is a source of immense anxiety and confusion. […]</p><a>READ MORE</a></div>
    </div>
    <div class="btn-pill"><b>APPLY NOW</b><span>And get a 30 minute consultation with one of our expert</span></div>
  </div>
</section>

<footer class="site-footer">
  <div class="wrap">
    <div class="foot-cols">
      <div>Home<br>About Us<br>Meet Our Team<br>Our Services<br>Why The Welborne Studio<br>Our 4-Step Process<br>3 Myths About the College Process</div>
      <div>Testimonials &amp; Case Studies<br>Welborne's Corner<br><span style="font-size:7.5px">(OTHER INTERNAL PAGES<br>TBD WILL GO HERE)</span></div>
      <div>48 W Larkin Ave, Chicago, IL 60610<br>Phone: (312) 555-0148<br>Contact Us | Request A Call
        <div class="social"><span></span><span></span><span></span><span></span></div></div>
    </div>
    <div class="foot-bottom">
      <div class="legal">Copyright © 2019 @thewelbornestudio. All rights reserved<br>Privacy Policy | Terms of Use</div>
      <div class="foot-brand">The Welborne Studio</div>
      <div class="foot-cta"><b>APPLY NOW</b><span>And get a 30 minute consultation with one of our expert</span></div>
    </div>
  </div>
</footer>

</body>
</html>
```